Brightwell is a company offering Colon Hydrotherapy (or colonics)

Brightwell offers Colon Hydrotherapy using an innovative FDA approved system from the USA. The system is called the TORVA system. The clinic is based in Whangarei, Northland and is the first business of this kind for Northland.
I used to use a design from the Printlane website - a water symbol. However, I want a design that will convey freshness. I want something new and clean which conveys vitality and revitalisation .... perhaps water or bubbles but which brings across the idea of detoxing (which is what colon hydrotherapy does)
The clinic will only be completed in April so for now I have put my mobile number but once in the clinic this will need to be changed to a landline number ... the email address will also change. Thanks for any ideas you give me,
Updates

Hi. I need the name Brightwell first and foremost as this is the name of the Company Underneath this it has to say Colon Hydrotherapy to let people know what Brightwell is My name underneath that would be Miriam Holloway And all contact details to follow this. Thanks !

Target Market(s)

People who are wanting to "detox" and focusing on their health and wellbeing

Industry/Entity Type

Clinic

Contact Information for Business Card

Brightwell
Colon Hydrotherapy
Miriam Holloway
Unit B, 42c Harbour Lane, Whangarei

021 0487 3926
brightwellcare@mailnest.example

Font styles to use
Serif

Colors
cee9f6
33a6d7
86cae6

Requirements
Must have
• Stand out with colour or logo

```html
<!DOCTYPE html>
<html lang="en">
<head>
<meta charset="utf-8">
<title>Brightwell Colon Hydrotherapy – Business Card</title>
<link rel="stylesheet" href="https://fonts.googleapis.com/css2?family=Cormorant+SC:wght@500&family=Tinos&display=swap">
<style>
  :root {
    --sky-pale: #cee9f6;
    --sky-mid: #86cae6;
    --brand-blue: #33a6d7;
    --ink: #1c1c1c;
    --crescent: #0b0b0b;
    --paper: #ffffff;
    --backdrop: #e9ecef;
  }
  html, body {
    margin: 0;
    width: 1200px;
    height: 1023px;
    overflow: hidden;
    background: var(--backdrop);
  }
  .canvas {
    position: relative;
    width: 1200px;
    height: 1023px;
  }
  .card {
    position: absolute;
    left: 170px;
    width: 860px;
    height: 470px;
    background: var(--paper);
    box-shadow: 0 6px 18px rgba(0,0,0,0.18);
    overflow: hidden;
  }
  .card--front { top: 30px; }
  .card--back { top: 523px; }
  .card__art {
    position: absolute;
    inset: 0;
    width: 100%;
    height: 100%;
  }
  .brand-line {
    position: absolute;
    margin: 0;
    font-family: "Cormorant SC", "Times New Roman", serif;
    font-weight: 500;
    font-size: 28px;
    line-height: 1.2;
    color: var(--brand-blue);
    letter-spacing: 0.02em;
    white-space: nowrap;
  }
  .card--front .brand-line {
    left: 58px;
    top: 104px;
  }
  .card--back .brand-line {
    left: 340px;
    top: 216px;
  }
  .holder-name {
    position: absolute;
    left: 60px;
    top: 144px;
    margin: 0;
    font-family: "Tinos", "Times New Roman", serif;
    font-size: 28px;
    font-weight: 400;
    color: var(--ink);
  }
  .contact-list {
    position: absolute;
    left: 60px;
    top: 300px;
    margin: 0;
    padding: 0;
    list-style: none;
    font-family: "Tinos", "Times New Roman", serif;
    font-size: 19px;
    line-height: 1.15;
    color: var(--ink);
  }
  .contact-list li {
    display: flex;
    align-items: flex-start;
    gap: 12px;
    margin-bottom: 6px;
  }
  .contact-icon {
    flex: none;
    width: 18px;
    height: 18px;
    margin-top: 2px;
    fill: var(--brand-blue);
  }
</style>
</head>
<body>
<main class="canvas">

  <section class="card card--front" aria-label="Business card front">
    <svg class="card__art" viewBox="0 0 860 470" preserveAspectRatio="none">
      <defs>
        <linearGradient id="waterFront" x1="0" y1="0" x2="1" y2="1">
          <stop offset="0" stop-color="#a9cdec"/>
          <stop offset="0.5" stop-color="#9fc3e6"/>
          <stop offset="1" stop-color="#c5dcf1"/>
        </linearGradient>
      </defs>
      <rect class="water-photo" x="0" y="0" width="860" height="470" fill="url(#waterFront)" role="img" aria-label="Photo of water droplets on a pale blue surface"/>
      <path class="crescent" d="M0,0 L505,0 Q730,235 578,470 L0,470 Z" fill="var(--crescent)"/>
      <path class="paper-panel" d="M0,0 L465,0 Q690,235 552,470 L0,470 Z" fill="var(--paper)"/>
    </svg>

    <h1 class="brand-line">Brightwell Colon Hydrotherapy</h1>
    <p class="holder-name">Miriam Holloway</p>

    <ul class="contact-list">
      <li>
        <svg class="contact-icon" viewBox="0 0 24 24" aria-hidden="true"><path d="M6.6 10.8a15.1 15.1 0 0 0 6.6 6.6l2.2-2.2a1 1 0 0 1 1-.25 11.4 11.4 0 0 0 3.6.57 1 1 0 0 1 1 1V20a1 1 0 0 1-1 1A17 17 0 0 1 3 4a1 1 0 0 1 1-1h3.5a1 1 0 0 1 1 1c0 1.250.2 2.450.57 3.6a1 1 0 0 1-.25 1z"/></svg>
        <span>021 0487 3926</span>
      </li>
      <li>
        <svg class="contact-icon" viewBox="0 0 24 24" aria-hidden="true"><path d="M2 5h20v14H2z M2 5l10 8 10-8" fill="none" stroke="#33a6d7" stroke-width="2.4"/></svg>
        <span>brightwellcare@mailnest.example</span>
      </li>
      <li>
        <svg class="contact-icon" viewBox="0 0 24 24" aria-hidden="true"><path d="M12 3 2 12h3v8h5v-5h4v5h5v-8h3z"/></svg>
        <span>Unit B, 42c Harbour Lane,<br>Whangarei</span>
      </li>
    </ul>
  </section>

  <section class="card card--back" aria-label="Business card back">
    <svg class="card__art" viewBox="0 0 860 470" preserveAspectRatio="none">
      <defs>
        <linearGradient id="waterBack" x1="0" y1="0" x2="1" y2="1">
          <stop offset="0" stop-color="#9fc3e6"/>
          <stop offset="1" stop-color="#c5dcf1"/>
        </linearGradient>
      </defs>
      <rect class="water-photo" x="0" y="0" width="860" height="470" fill="url(#waterBack)" role="img" aria-label="Photo of water droplets on a pale blue surface"/>
      <path class="crescent" d="M860,0 L300,0 Q130,235 275,470 L860,470 Z" fill="var(--crescent)"/>
      <path class="paper-panel" d="M860,0 L340,0 Q160,235 300,470 L860,470 Z" fill="var(--paper)"/>
    </svg>

    <p class="brand-line">Brightwell Colon Hydrotherapy</p>
  </section>

</main>
</body>
</html>
```